Kestrel Drafts (Residential House Plans Company)

Want professional landing page to match our company theme. We provide custom house plans for primarily residential. We are structural engineers (not architects).

Prefer dark (black) theme but open to design options. Would like map of office location.

Address: 214 W Marlow Street, Oviedo, FL 32768
Phone: 407-582-6194
Email: office@kestreldrafts.example

Target Market(s)

Client who need custom house plans

Industry/Entity Type

Architecture, Structural Engineering

Coding

Coded - Design and coding required

Colors
0054AA
0677BA
7BADD7
CADEEF
E8F1F8

```html
<!DOCTYPE html>
<html lang="en">
<head>
<meta charset="UTF-8">
<title>Kestrel Drafts – Custom House Plans</title>
<link href="https://fonts.googleapis.com/css2?family=Poppins:wght@300;400;500&display=swap" rel="stylesheet">
<style>
:root{
  --bg:#03080e;
  --bg-deep:#010409;
  --blue-dark:#0054AA;
  --blue:#0677BA;
  --blue-mid:#7BADD7;
  --blue-light:#CADEEF;
  --blue-pale:#E8F1F8;
  --text:#ffffff;
  --muted:#7BADD7;
  --line:#123252;
}
*{margin:0;padding:0;box-sizing:border-box}
html,body{width:1200px;height:3604px;overflow:hidden}
body{
  font-family:"Poppins",sans-serif;color:var(--text);position:relative;
  background:
    radial-gradient(ellipse 520px 380px at 600px 260px,rgba(6,119,186,.35),transparent 70%),
    radial-gradient(ellipse 500px 400px at 250px 820px,rgba(0,84,170,.18),transparent 70%),
    radial-gradient(ellipse 500px 450px at 560px 1600px,rgba(0,84,170,.16),transparent 70%),
    radial-gradient(ellipse 520px 420px at 200px 2500px,rgba(0,84,170,.18),transparent 70%),
    radial-gradient(ellipse 600px 400px at 900px 3200px,rgba(0,84,170,.14),transparent 70%),
    var(--bg);
}
.abs{position:absolute}
.logo{display:flex;align-items:center;gap:8px;font-weight:500;font-size:22px;color:var(--text)}
.logo-mark{width:14px;height:14px;background:var(--blue);border-radius:3px}
.nav{left:0;top:0;width:1200px;height:92px}
.nav .logo{position:absolute;left:106px;top:32px}
.nav-links{position:absolute;right:105px;top:38px;display:flex;gap:30px;font-size:12.5px}
.nav-links a,.footer-links a{color:var(--text);text-decoration:none}
.btn{display:inline-flex;align-items:center;justify-content:center;height:39px;border-radius:20px;font-size:13px;color:#fff;background:var(--blue);text-decoration:none}
.btn-outline{background:transparent;border:1.5px solid var(--blue);color:var(--blue)}
.hero-light{left:357px;top:152px;width:489px;height:5px;background:linear-gradient(90deg,transparent,var(--blue-mid),transparent);box-shadow:0 8px 60px 20px rgba(6,119,186,.35)}
.hero-title{left:0;width:1200px;top:226px;text-align:center;font-size:51px;font-weight:400;line-height:60px}
.hero-text{left:0;width:1200px;top:352px;text-align:center;font-size:13.5px;line-height:27px;color:var(--muted);font-weight:300}
.eyebrow{font-size:19px;font-weight:400}
.h2{font-size:36px;font-weight:400;line-height:46px}
.para{font-size:13.5px;line-height:27px;color:var(--muted);font-weight:300}
.ph{border-radius:2px}
.about-art{left:130px;top:660px;width:376px;height:326px;background:radial-gradient(ellipse at 60% 60%,rgba(6,119,186,.55),rgba(0,84,170,.15) 60%,transparent 80%)}
.plans-head{left:0;width:1200px;text-align:center}
.sphere{border-radius:50%;background:radial-gradient(circle at 35% 35%,#2a8fd0,var(--blue-dark) 70%);}
.card{top:1287px;width:322px;height:611px;border:1.5px solid var(--line);border-radius:42px;background:rgba(2,8,16,.82)}
.card-name{position:absolute;left:36px;top:36px;font-size:19px}
.card-price{position:absolute;left:32px;top:76px;font-size:33px;font-weight:500}
.card-rule{position:absolute;left:32px;top:137px;width:220px;height:1px;background:linear-gradient(90deg,var(--blue),transparent)}
.features{position:absolute;left:28px;top:172px;list-style:none}
.features li{display:flex;align-items:center;gap:10px;height:59px;margin-top:-17px;padding-top:0;font-size:13px;color:var(--muted);font-weight:300}
.features li:first-child{margin-top:0;height:24px}
.features li{height:24px;margin-bottom:35px;margin-top:0}
.card .btn{position:absolute;left:101px;top:532px;width:120px}
.card-glow{position:absolute;width:220px;height:220px;border-radius:50%;background:radial-gradient(circle,rgba(6,119,186,.3),transparent 70%)}
.newsletter{left:190px;top:2000px;width:820px;height:248px;border-radius:42px;background:linear-gradient(90deg,var(--blue) 0%,#2f8fcb 60%,var(--blue-mid) 100%);box-shadow:0 10px 40px rgba(6,119,186,.35);overflow:hidden}
.newsletter-art{position:absolute;left:510px;top:0;width:230px;height:180px;background:linear-gradient(180deg,rgba(232,241,248,.18),rgba(232,241,248,0));border-radius:4px}
.newsletter .eyebrow{position:absolute;left:49px;top:28px;font-size:13px}
.newsletter .h2{position:absolute;left:49px;top:68px;font-size:34px;line-height:46px}
.subscribe{position:absolute;left:44px;top:178px;width:732px;height:40px;display:flex;border-radius:6px;overflow:hidden}
.subscribe span{flex:1;background:var(--blue-pale);color:var(--blue-mid);font-size:13px;padding-left:27px;display:flex;align-items:center}
.subscribe b{width:117px;background:var(--blue);font-weight:500;font-size:13px;display:flex;align-items:center;justify-content:center}
.photo{background:linear-gradient(160deg,#4a3a2c,#1c2a3a 60%,#0d1d2e)}
.photo-day{background:linear-gradient(170deg,#d8d2c4,#b9a88a 50%,#4f6a3a)}
.photo-night{background:linear-gradient(170deg,#33516b,#1a2f45 50%,#0e1c2b)}
.map{left:0;top:3045px;width:519px;height:307px;background:linear-gradient(135deg,#c9d6e4,#9fb8cf 50%,#a9c7a4);border-right:7px solid var(--blue);border-top:7px solid var(--blue)}
.contact-list{left:608px;top:3217px;list-style:none}
.contact-list li{display:flex;align-items:center;gap:10px;height:26px;margin-bottom:24px;font-size:14px;font-weight:300}
.ico{width:22px;height:22px;border-radius:50%;background:var(--blue);display:flex;align-items:center;justify-content:center}
.footer-rule{left:0;top:3441px;width:1200px;height:1px;background:linear-gradient(90deg,transparent,var(--line) 20%,var(--line) 80%,transparent)}
.footer .logo{position:absolute;left:106px;top:3486px}
.footer-links{left:439px;top:3492px;display:flex;gap:31px;font-size:12.5px}
.social{top:3485px;width:32px;height:32px;border-radius:50%;background:var(--blue)}
.copyright{left:0;width:1200px;top:3566px;text-align:center;font-size:11.5px;color:var(--muted);font-weight:300}
</style>
</head>
<body>

<header class="abs nav">
  <div class="logo"><span class="logo-mark"></span>Kestrel Drafts</div>
  <nav class="nav-links"><a href="#">Home</a><a href="#">About</a><a href="#">Plans</a><a href="#">Projects</a><a href="#">Contact</a></nav>
</header>

<section class="hero">
  <div class="abs hero-light"></div>
  <h1 class="abs hero-title">We Provide Custom Plans<br>For Your Dream House</h1>
  <p class="abs hero-text">Lorem Ipsum Dolor Sit Amet Consectetur. Tempor Curabitur In In Auctor<br>Volutpat Eleifend Vestibulum. Sed Magna Odio Massa Egest</p>
  <a class="abs btn" style="left:473px;top:418px;width:120px">Learn More</a>
  <a class="abs btn btn-outline" style="left:611px;top:418px;width:115px">View Plans</a>
</section>

<section class="about">
  <div class="abs about-art ph" role="img" aria-label="Blueprint drawing of a house elevation over a state outline"></div>
  <div class="abs eyebrow" style="left:606px;top:681px">About</div>
  <h2 class="abs h2" style="left:604px;top:722px">Know What Make Us<br>Different From Others</h2>
  <p class="abs para" style="left:606px;top:825px;width:480px">Lorem Ipsum Dolor Sit Amet Consectetur. Sit Neque Aenean Faucibus Amet Posuere Imperdiet Elit. Volutpat Facilisi In Sem In Eget. Mattis Urna Quis Arcu Ultrices. Tellus Nulla Ultricies Tincidunt Aliquet Eget Vel Integer. Enim Ut Amet Cursus Id Mi. Pellentesque Iaculis Eu Gravida Elementum.</p>
  <a class="abs btn" style="left:606px;top:950px;width:120px">Learn More</a>
</section>

<section class="plans">
  <div class="abs plans-head eyebrow" style="top:1100px">Plans</div>
  <h2 class="abs plans-head h2" style="top:1142px">Choose The Right Plan For Your Need</h2>
  <p class="abs plans-head para" style="top:1202px">Lorem Ipsum Dolor Sit Amet Consectetur. Sit Neque Aenean Faucibus Amet Posuere Imperdiet Elit.<br>Volutpat Facilisi In Sem In Eget. Mattis Urna Quis Arcu Ultrices. Tellus Nulla Ultricies</p>

  <div class="abs sphere" style="left:48px;top:1343px;width:104px;height:104px"></div>
  <div class="abs sphere" style="left:1025px;top:1777px;width:110px;height:110px"></div>

  <svg width="0" height="0" style="position:absolute">
    <symbol id="tick" viewBox="0 0 20 20"><circle cx="10" cy="10" r="10" fill="#0677BA"/><path d="M5.5 10.3l3 3 6-6.3" fill="none" stroke="#E8F1F8" stroke-width="1.8" stroke-linecap="round" stroke-linejoin="round"/></symbol>
  </svg>

  <article class="abs card" style="left:106px">
    <div class="card-glow" style="left:-20px;top:40px"></div>
    <div class="card-name">Basic</div>
    <div class="card-price">499$</div>
    <div class="card-rule"></div>
    <ul class="features">
      <li><svg width="19" height="19"><use href="#tick"/></svg>Amet Consectetur Neque Faucibus</li>
      <li><svg width="19" height="19"><use href="#tick"/></svg>Amet Neque Faucibus</li>
      <li><svg width="19" height="19"><use href="#tick"/></svg>Amet Consectetur Faucibus</li>
      <li><svg width="19" height="19"><use href="#tick"/></svg>Amet Consectetur Neque Faucibus</li>
    </ul>
    <a class="btn">Get Started</a>
  </article>

  <article class="abs card" style="left:439px">
    <div class="card-glow" style="left:60px;top:200px"></div>
    <div class="card-name">Pro</div>
    <div class="card-price">999$</div>
    <div class="card-rule"></div>
    <ul class="features">
      <li><svg width="19" height="19"><use href="#tick"/></svg>Amet Consectetur Neque Faucibus</li>
      <li><svg width="19" height="19"><use href="#tick"/></svg>Amet Neque Faucibus</li>
      <li><svg width="19" height="19"><use href="#tick"/></svg>Amet Consectetur Faucibus</li>
      <li><svg width="19" height="19"><use href="#tick"/></svg>Amet Neque Faucibus</li>
      <li><svg width="19" height="19"><use href="#tick"/></svg>Amet Consectetur Neque Faucibus</li>
    </ul>
    <a class="btn">Get Started</a>
  </article>

  <article class="abs card" style="left:772px">
    <div class="card-glow" style="left:150px;top:420px"></div>
    <div class="card-name">Ultimate</div>
    <div class="card-price">1499$</div>
    <div class="card-rule"></div>
    <ul class="features">
      <li><svg width="19" height="19"><use href="#tick"/></svg>Amet Consectetur Neque Faucibus</li>
      <li><svg width="19" height="19"><use href="#tick"/></svg>Amet Neque Faucibus</li>
      <li><svg width="19" height="19"><use href="#tick"/></svg>Amet Consectetur Faucibus</li>
      <li><svg width="19" height="19"><use href="#tick"/></svg>Amet Neque Faucibus</li>
      <li><svg width="19" height="19"><use href="#tick"/></svg>Amet Consectetur Neque Faucibus</li>
      <li><svg width="19" height="19"><use href="#tick"/></svg>Amet Consectetur Faucibus</li>
    </ul>
    <a class="btn">Get Started</a>
  </article>
</section>

<section class="abs newsletter">
  <div class="newsletter-art" role="img" aria-label="Faint line drawing of a house"></div>
  <div class="eyebrow">Subscribe Our Newsletter</div>
  <h2 class="h2">Subscribe To Don’t<br>Miss An Update</h2>
  <div class="subscribe"><span>example123@email.com</span><b>Subscribe</b></div>
</section>

<section class="projects">
  <div class="abs eyebrow" style="left:106px;top:2337px">Projects</div>
  <h2 class="abs h2" style="left:105px;top:2379px">Explore Our Best Works</h2>
  <p class="abs para" style="left:106px;top:2439px;width:420px">Lorem Ipsum Dolor Sit Amet Consectetur. Sit Neque Aenean Faucibus Amet Posuere Imperdiet Elit. Volutpat Facilisi In Sem In Eget. Mattis Urna</p>
  <a class="abs btn" style="left:106px;top:2546px;width:120px">Learn More</a>
  <div class="abs ph photo" style="left:606px;top:2337px;width:487px;height:299px" role="img" aria-label="Photo of a modern house with wood cladding and a pool at dusk"></div>
  <div class="abs ph photo-day" style="left:106px;top:2648px;width:488px;height:299px" role="img" aria-label="Photo of a white modern house with large glass windows beside a tree"></div>
  <div class="abs ph photo-night" style="left:606px;top:2648px;width:488px;height:299px" role="img" aria-label="Photo of a multi-level glass house on a rocky hillside at night"></div>
</section>

<section class="contact">
  <div class="abs map" role="img" aria-label="Map showing the office location in Oviedo, Florida"></div>
  <div class="abs eyebrow" style="left:608px;top:3052px">Contact</div>
  <h2 class="abs h2" style="left:608px;top:3088px">Connect With Us To Make<br>Your Dream House</h2>
  <ul class="abs contact-list">
    <li><span class="ico"><svg width="12" height="12" viewBox="0 0 12 12"><path d="M6 1a3.5 3.5 0 0 0-3.5 3.5C2.5 7.2 6 11 6 11s3.5-3.8 3.5-6.5A3.5 3.5 0 0 0 6 1z" fill="#fff"/><circle cx="6" cy="4.5" r="1.2" fill="#0677BA"/></svg></span>214 W Marlow Street, Oviedo, FL 32768</li>
    <li><span class="ico"><svg width="12" height="12" viewBox="0 0 12 12"><rect x="3.5" y="1" width="5" height="10" rx="1" fill="#fff"/><rect x="4.5" y="2.3" width="3" height="6" fill="#0677BA"/></svg></span>407-582-6194</li>
    <li><span class="ico"><svg width="12" height="12" viewBox="0 0 12 12"><rect x="1.5" y="3" width="9" height="6.5" rx="1" fill="#fff"/><path d="M1.8 3.5L6 6.7l4.2-3.2" fill="none" stroke="#0677BA" stroke-width="1"/></svg></span>office@kestreldrafts.example</li>
  </ul>
</section>

<footer class="footer">
  <div class="abs footer-rule"></div>
  <div class="logo"><span class="logo-mark"></span>Kestrel Drafts</div>
  <nav class="abs footer-links"><a href="#">Home</a><a href="#">About</a><a href="#">Plans</a><a href="#">Projects</a><a href="#">Contact</a></nav>
  <a class="abs social" style="left:942px" aria-label="Social profile one"></a>
  <a class="abs social" style="left:1001px" aria-label="Social profile two"></a>
  <a class="abs social" style="left:1060px" aria-label="Social profile three"></a>
  <div class="abs copyright">© 2023 Kestrel Drafts. All rights reserved.</div>
</footer>

</body>
</html>
```